Plakat-Design für Vermieter von Ferienwohnungen im Allgäu
Zielgruppe
Wir vermieten Ferienwohnungen im Allgäu.
www.residenz-wiesental.de
Aufgabenstellung
Das Schild (Querformat) sollte freundlich, ansprechend und modern sein. Größe 140x180 cm.
Es wird eine Begrüßung für den Gast, wenn er in die Tiefgarage fährt.
Text:
Herzlich Willkommen
in der Residenz Lerchenau
Als Hintergrund können wir uns Berge, Landschaft oder ähnliches vorstellen.

```html
<!DOCTYPE html>
<html lang="de">
<head>
<meta charset="utf-8">
<title>Herzlich Willkommen – Schildentwürfe</title>
<link rel="stylesheet" href="https://fonts.googleapis.com/css2?family=Archivo+Black&display=swap">
<style>
  :root {
    --stage-top: #f2f2f2;
    --stage-bottom: #858585;
    --sky-top: #8fb0dc;
    --sky-mid: #b9d8ee;
    --haze: rgba(255, 255, 255, 0.86);
    --navy: #0f2440;
    --forest: #3a3f18;
    --frame: #000000;
    --white: #ffffff;
  }
  * { box-sizing: border-box; margin: 0; padding: 0; }
  html, body { width: 1200px; height: 1200px; overflow: hidden; }
  body {
    position: relative;
    background: linear-gradient(to bottom, var(--stage-top) 0%, #d6d6d6 35%, #a9a9a9 70%, var(--stage-bottom) 100%);
    font-family: "Archivo Black", "Arial Black", sans-serif;
  }
  .sign { position: absolute; top: 247px; height: 756px; overflow: hidden; }
  .line { display: block; }

  /* Variante 1: Landschaft */
  .sign--landscape {
    left: 0; width: 584px;
    background: linear-gradient(to bottom, var(--sky-top) 0%, var(--sky-mid) 40%, #d8eaf6 70%, #e9f2f8 100%);
  }
  .sign__haze {
    position: absolute; left: 21px; top: 24px; width: 540px; height: 520px;
    background: var(--haze);
  }
  .sign__scenery {
    position: absolute; left: 0; right: 0; top: 460px; bottom: 0;
    background: linear-gradient(to bottom, #7d88a8 0%, #4f6a5a 25%, #34502e 55%, #263a1b 100%);
  }
  .sign--landscape .greeting {
    position: absolute; left: 0; right: 0; top: 306px;
    text-align: center; color: var(--navy); line-height: 1;
  }
  .sign--landscape .greeting__lead { font-size: 34px; }
  .sign--landscape .greeting__small { font-size: 27px; margin-top: 14px; }
  .sign--landscape .greeting__name { font-size: 34px; margin-top: 14px; }

  /* Variante 2: Waldgrün */
  .sign--forest { left: 612px; width: 588px; background: var(--frame); }
  .sign__panel {
    position: absolute; left: 30px; top: 18px; width: 530px; height: 726px;
    background: var(--forest); border-radius: 40px;
  }
  .sign--forest .greeting {
    position: absolute; left: 0; right: 0; top: 160px;
    text-align: center; color: var(--white); line-height: 1;
    text-shadow: 3px 4px 5px rgba(0, 0, 0, 0.75);
  }
  .sign--forest .greeting__top { font-size: 36px; }
  .sign--forest .greeting__big { font-size: 48px; margin-top: 12px; }
  .sign--forest .greeting__small { font-size: 28px; margin-top: 12px; }
  .sign--forest .greeting__name { font-size: 44px; margin-top: 12px; }
  .sign__peaks {
    position: absolute; left: 22px; top: 443px; width: 486px; height: 137px;
    background: linear-gradient(to bottom, rgba(191, 191, 196, 0.5), rgba(191, 191, 196, 0.15));
    border-radius: 6px;
  }
</style>
</head>
<body>
  <section class="sign sign--landscape">
    <div class="sign__haze"></div>
    <div class="sign__scenery" role="img" aria-label="Illustrierte Allgäuer Berglandschaft mit See und Wald"></div>
    <h1 class="greeting">
      <span class="line greeting__lead">Herzlich Willkommen</span>
      <span class="line greeting__small">in der</span>
      <span class="line greeting__name">Residenz Lerchenau</span>
    </h1>
  </section>

  <section class="sign sign--forest">
    <div class="sign__panel">
      <h1 class="greeting">
        <span class="line greeting__top">Herzlich</span>
        <span class="line greeting__big">Willkommen</span>
        <span class="line greeting__small">in der</span>
        <span class="line greeting__name">Residenz Lerchenau</span>
      </h1>
      <div class="sign__peaks" role="img" aria-label="Grafische Bergsilhouette"></div>
    </div>
  </section>
</body>
</html>
```